MyUptownGroove Web Site Header

Potential designers can visit the site (MyUptownGroove.com) to see our current header. The orange color CANNOT CHANGE! Please do not submit anything different colors. The header needs to contain the following items:
-MyUptownGroove.com
-Do You Sense The Pulse (There IS NO "?" BEHIND THIS!)
- 555.284.6390

I've supplied 13 different photos that you can choose from as a background.

Images of 920 x 150 pixels are the "exact size" that will fit my site. If it's larger, and I have to crop on uploading, I could lose text along the edges. (for what that info is worth!)

Background: Midtown Atlanta is the urban living core of Atlanta. Filled with highrise condominiums, restaurants, shopping and is also called the Heart of the Arts because Wren Playhouse and Calloway Gallery are located there. It's a diverse mixture of people that live there, as well as all the office buildings that are filled daily.

The final design should give a feel of excitement, hence our tagline, Do You Sense The Pulse.
Updates

Project Deadline Extended
Reason: I've gotten some INCREDIBLE designs. It's been hard to make a decision. In fact, may have to select more than one. I'm also in the middle of another project and have been swamped with it.

Target Market(s)

Target market is condo buyers. Age range from 20's to 50's. Heavy concentration of law offices and high-tech companies in the area...so think techy consumer.

Industry/Entity Type

Shopping

Font styles to use
Sans Serif

Colors
f37022

Requirements
Must have
• Phone Number 555.284.6390 or 555-284-6390

MyUptownGroove.com site name in header

```html
<!DOCTYPE html>
<html lang="en">
<head>
<meta charset="utf-8">
<title>MyUptownGroove Header</title>
<link rel="stylesheet" href="https://fonts.googleapis.com/css2?family=Open+Sans:wght@700&family=Bebas+Neue&display=swap">
<style>
  :root {
    --brand-orange: #f37022;
    --orange-deep: #e0621a;
    --sky-light: #74b6ee;
    --sky-mid: #4f9be0;
    --city-tone: #8ea3b2;
    --tree-tone: #6f7f4a;
    --ink-white: #ffffff;
  }
  * { margin: 0; padding: 0; box-sizing: border-box; }
  html, body { width: 1200px; height: 196px; overflow: hidden; background: #ffffff; }
  .header {
    position: relative;
    width: 1200px;
    height: 196px;
    overflow: hidden;
    background: var(--brand-orange);
  }
  .top-bar {
    position: absolute;
    left: 0; top: 0;
    width: 1200px; height: 39px;
    background: var(--brand-orange);
  }
  .top-bar .dash-row { position: absolute; left: 0; top: 0; }
  .phone, .site-name {
    position: absolute;
    top: 0;
    font-family: "Open Sans", Arial, sans-serif;
    font-weight: 700;
    font-size: 26px;
    line-height: 39px;
    color: var(--ink-white);
    text-transform: uppercase;
    white-space: nowrap;
  }
  .phone { left: 15px; }
  .site-name { right: 14px; }
  .scene {
    position: absolute;
    left: 0; top: 39px;
    width: 1200px; height: 157px;
    background:
      linear-gradient(180deg, rgba(255,255,255,0) 50%, rgba(111,127,74,0.9) 100%) 0 0 / 565px 100% no-repeat,
      linear-gradient(90deg, var(--city-tone) 0%, #9fb4c4 32%, var(--sky-mid) 50%, var(--sky-light) 100%);
  }
  .tagline {
    position: absolute;
    right: 32px;
    top: 92px;
    font-family: "Bebas Neue", "Oswald", sans-serif;
    font-size: 80px;
    line-height: 80px;
    color: var(--ink-white);
    letter-spacing: 1px;
    white-space: nowrap;
    text-shadow: 0 1px 3px rgba(0,0,0,0.25);
  }
</style>
</head>
<body>
  <header class="header">
    <div class="top-bar">
      <svg class="dash-row" width="1200" height="39" aria-hidden="true">
        <line x1="308" y1="21" x2="783" y2="21" stroke="var(--orange-deep)" stroke-width="14" stroke-dasharray="14 6"/>
      </svg>
      <div class="phone">Call: 555.284.6390</div>
      <div class="site-name">MyUptownGroove.com</div>
    </div>

    <div class="scene" role="img" aria-label="Photo of the uptown city skyline with high-rise condo towers above autumn trees under a clear blue sky"></div>

    <div class="tagline">Do You Sense The Pulse</div>
  </header>
</body>
</html>
```